Sole trader requires buisness card / company logo for mining and aviation

I require a business card and logo design having the following requirements;
Skyward and Engine Works
Owner: Martin Hollis
Ph: 0471593064
E: martin-r-hollis@quillmail.com.au

Logo should include a basic aircraft image and an image of an item of mining machinery either a dump truck or large excavator, but keeping in mind that the image is to be transferred onto clothing embroidery.

```html
<!DOCTYPE html>
<html lang="en">
<head>
<meta charset="utf-8">
<title>Skyward and Engine Works – Business Card</title>
<link href="https://fonts.googleapis.com/css2?family=Open+Sans:wght@400;600;700&display=swap" rel="stylesheet">
<style>
  :root {
    --stage: #e9e7e4;
    --card-dark: #1b1b1c;
    --card-dark-edge: #2c2c2e;
    --brand-red: #ec2227;
    --logo-red: #f20d0d;
    --ink-light: #f4f4f4;
    --card-white: #ffffff;
  }
  * { margin: 0; padding: 0; box-sizing: border-box; }
  html, body {
    width: 1200px;
    height: 1000px;
    overflow: hidden;
    background: var(--stage);
    font-family: "Open Sans", Arial, sans-serif;
  }
  .canvas { position: relative; width: 1200px; height: 1000px; }

  .card {
    position: absolute;
    width: 780px;
    height: 450px;
    border-radius: 28px;
    overflow: hidden;
    box-shadow: 0 10px 24px rgba(0,0,0,0.28);
  }

  /* Front */
  .card-front {
    left: 80px; top: 60px;
    background: radial-gradient(ellipse at 45% 50%, var(--card-dark-edge), var(--card-dark) 75%);
    z-index: 2;
  }
  .torn-band { position: absolute; left: 0; width: 100%; height: 110px; display: block; }
  .torn-band--top { top: 0; }
  .torn-band--bottom { bottom: 0; }
  .torn-band polygon { fill: var(--brand-red); }

  .front-brand {
    position: absolute;
    left: 70px; top: 190px;
    width: 340px;
    display: flex;
    align-items: center;
    gap: 14px;
  }
  .brand-square {
    flex: 0 0 auto;
    width: 22px; height: 22px;
    background: var(--ink-light);
  }
  .brand-name {
    font-weight: 700;
    font-size: 30px;
    line-height: 1.15;
    color: var(--ink-light);
  }

  .contact {
    position: absolute;
    left: 460px; top: 178px;
    color: var(--ink-light);
  }
  .contact-name {
    font-weight: 700;
    font-size: 27px;
    color: var(--brand-red);
    margin-bottom: 38px;
  }
  .contact-line {
    display: flex;
    align-items: center;
    gap: 10px;
    font-size: 16px;
    margin-bottom: 10px;
    white-space: nowrap;
  }
  .contact-icon { width: 16px; height: 16px; flex: 0 0 auto; }
  .contact-icon path, .contact-icon rect { fill: var(--brand-red); }

  /* Back */
  .card-back {
    left: 340px; top: 500px;
    background: var(--card-white);
    z-index: 1;
    display: flex;
    align-items: center;
    justify-content: center;
  }
  .back-brand {
    display: flex;
    align-items: center;
    gap: 18px;
  }
  .back-brand .brand-square { width: 30px; height: 30px; background: var(--logo-red); }
  .back-brand .brand-name { color: var(--logo-red); font-size: 40px; }
</style>
</head>
<body>
<main class="canvas">

  <section class="card card-front" aria-label="Business card front">
    <svg class="torn-band torn-band--top" viewBox="0 0 780 110" preserveAspectRatio="none" aria-hidden="true">
      <polygon points="0,0 780,0 780,58 760,62 742,55 720,64 700,58 676,66 650,60 628,70 604,64 580,74 556,68 530,78 506,72 480,82 456,77 430,86 404,80 380,90 352,84 326,94 300,88 272,96 246,90 220,99 192,93 166,101 138,95 112,104 86,97 60,106 34,99 14,106 0,100"/>
    </svg>

    <div class="front-brand">
      <span class="brand-square"></span>
      <span class="brand-name">Skyward and Engine Works</span>
    </div>

    <div class="contact">
      <p class="contact-name">Martin Hollis</p>
      <p class="contact-line">
        <svg class="contact-icon" viewBox="0 0 16 16" aria-hidden="true">
          <path d="M3 1h3l1.5 4-2 1.3a9 9 0 0 0 4.2 4.2L11 8.5l4 1.5v3c0 1-1 2-2 2C6.4 15 1 9.6 1 3c0-1 1-2 2-2z"/>
        </svg>
        0471593064
      </p>
      <p class="contact-line">
        <svg class="contact-icon" viewBox="0 0 16 16" aria-hidden="true">
          <path d="M1 3h14v1.2L8 9 1 4.2z"/>
          <path d="M1 5.6l7 4.8 7-4.8V13H1z"/>
        </svg>
        martin-r-hollis@quillmail.com.au
      </p>
    </div>

    <svg class="torn-band torn-band--bottom" viewBox="0 0 780 110" preserveAspectRatio="none" aria-hidden="true">
      <polygon points="0,110 780,110 780,8 758,14 736,6 712,16 690,10 664,20 640,14 614,24 590,18 564,28 538,22 512,32 486,26 460,36 434,30 408,40 382,34 356,44 330,38 304,48 278,42 250,52 224,46 198,56 170,50 144,60 118,54 92,64 66,58 40,68 18,62 0,70"/>
    </svg>
  </section>

  <section class="card card-back" aria-label="Business card back">
    <div class="back-brand">
      <span class="brand-square"></span>
      <span class="brand-name">Skyward and Engine Works</span>
    </div>
  </section>

</main>
</body>
</html>
```